Tervolan Pty Ltd professional business card

A professional business card template using the colours from the supplied logo.
Clean crisp lines while, Modern while not being over the top.

Target Market(s)

Construction, commerical and industrial

Industry/Entity Type

Communications

Contact Information for Business Card

For a Communications, IT, Optical fibre installation company

Colors
37b8a4

```html
<!DOCTYPE html>
<html lang="en">
<head>
<meta charset="utf-8">
<title>Tervolan Pty Ltd business card</title>
<link rel="stylesheet" href="https://fonts.googleapis.com/css2?family=Lato:wght@400;700&display=swap">
<style>
  :root {
    --backdrop: #c9c9c9;
    --card-dark: #231f20;
    --card-light: #fbfbfb;
    --teal: #2196a3;
    --grey: #6d6e71;
    --ink: #4a4a4c;
    --wordmark-dark: #7c7d80;
  }
  * { box-sizing: border-box; margin: 0; padding: 0; }
  html, body {
    width: 1200px; height: 1195px; overflow: hidden;
    background: var(--backdrop);
    font-family: "Lato", sans-serif;
  }
  .card {
    position: absolute; left: 250px;
    width: 700px; height: 400px;
    border-radius: 22px;
    box-shadow: 0 6px 18px rgba(0,0,0,.18);
  }
  .card-back { top: 150px; background: var(--card-dark); }
  .card-front { top: 630px; background: var(--card-light); }

  .card-back .wordmark {
    position: absolute; left: 0; right: 0; top: 140px;
    text-align: center;
    font-weight: 700; font-size: 78px; letter-spacing: 4px;
    color: var(--wordmark-dark);
  }
  .card-back .website {
    position: absolute; left: 0; right: 0; top: 318px;
    text-align: center; font-size: 20px; letter-spacing: 1px;
    color: var(--teal);
  }

  .card-front .wordmark {
    position: absolute; right: 44px; top: 52px;
    font-weight: 700; font-size: 54px; letter-spacing: 3px;
    color: var(--grey);
  }
  .person { position: absolute; left: 48px; top: 145px; }
  .person-name { font-size: 32px; color: var(--teal); letter-spacing: 1px; }
  .person-role { font-size: 22px; color: var(--ink); letter-spacing: 1px; margin-top: 2px; }
  .rule {
    position: absolute; left: 165px; right: 0; top: 216px;
    height: 2px; background: var(--teal);
  }
  .contact-list { position: absolute; left: 48px; top: 248px; list-style: none; }
  .contact-list li {
    display: flex; align-items: center; gap: 10px;
    font-size: 21px; color: var(--ink); letter-spacing: 1px;
    height: 38px;
  }
  .contact-list svg { width: 26px; height: 26px; flex: none; }
  .address {
    position: absolute; right: 48px; bottom: 44px;
    text-align: right; font-size: 22px; line-height: 1.45;
    color: var(--ink); letter-spacing: 1px;
  }
</style>
</head>
<body>
  <section class="card card-back">
    <div class="wordmark">TERVOLAN</div>
    <div class="website">www.yourdomain.com</div>
  </section>

  <section class="card card-front">
    <div class="wordmark">TERVOLAN</div>
    <div class="person">
      <div class="person-name">Marlen Ostrow</div>
      <div class="person-role">Director</div>
    </div>
    <div class="rule"></div>
    <ul class="contact-list">
      <li>
        <svg viewBox="0 0 26 26" fill="none" stroke="var(--teal)" stroke-width="1.6">
          <circle cx="13" cy="13" r="11.5"/>
          <path d="M9 7.5l2 2.8-1.2 1.4c.8 1.8 2.2 3.2 4 4l1.4-1.2 2.8 2-1.2 2c-4.5.2-9.3-4.6-9.1-9.1z" fill="var(--teal)" stroke="none"/>
        </svg>
        014.5678 902
      </li>
      <li>
        <svg viewBox="0 0 26 26" fill="none" stroke="var(--teal)" stroke-width="1.6">
          <circle cx="13" cy="13" r="11.5"/>
          <rect x="7" y="9" width="12" height="8.5" rx="1"/>
          <path d="M7 9.5l6 4.5 6-4.5"/>
        </svg>
        info@yourdomain.com
      </li>
      <li>
        <svg viewBox="0 0 26 26" fill="none" stroke="var(--teal)" stroke-width="1.4">
          <circle cx="13" cy="13" r="11.5"/>
          <ellipse cx="13" cy="13" rx="5" ry="11.5"/>
          <path d="M1.5 13h23M3.5 7h19M3.5 19h19"/>
        </svg>
        www.yourdomain.com
      </li>
    </ul>
    <div class="address">
      1023 Street Here, Suite 123<br>
      City Name, State 1234
    </div>
  </section>
</body>
</html>
```